Architecture firm needing a business card

We need a business card design for a new company based in the US called "Pellmore Architecture". Seeking minimalist designs that have a creativity/design feel but must be clean and professional. Please refer to the logo attached.

Target Market(s)

Real Estate Investors, Home Builders and Construction Firms.

Industry/Entity Type

Architecture

Contact Information for Business Card

Standard US size business cards. Would like to have some sort of graphic on the back side of the card - nothing that is too loud but something that may catch your attention. More or less grayscale colors that are in line with the logo colors (navy and greys essentially). Additional colors maybe accepted if blended properly (earthtones), but might be difficult to accomplish and maintain the clean/minimalist look.

Requirements
Must have
• Clean Lines
Nice to have
• some sort of graphics, would like to have something creative on the back side of the card
Should not have
• nothing too busy, cluttered or overwhelming.

```html
<!DOCTYPE html>
<html lang="en">
<head>
<meta charset="utf-8">
<title>Pellmore Architecture – Business Card</title>
<link rel="stylesheet" href="https://fonts.googleapis.com/css2?family=Josefin+Sans:wght@400&display=swap">
<style>
  :root {
    --page: #ffffff;
    --card: #ffffff;
    --edge: #8a8a8a;
    --navy: #1b4468;
    --grey: #8e8e8e;
    --slate: #5d6a86;
    --mist: #b7b9c8;
    --lilac: #a995c2;
    --steel: #6f8fb0;
    --dusk: #4a4f7c;
  }
  html, body {
    margin: 0;
    padding: 0;
    width: 1200px;
    height: 1000px;
    overflow: hidden;
    background: var(--page);
  }
  .canvas {
    position: relative;
    width: 1200px;
    height: 1000px;
  }
  .card {
    position: absolute;
    left: 256px;
    top: 271px;
    width: 780px;
    height: 398px;
    background: var(--card);
    border-left: 1px solid var(--edge);
    border-right: 1px solid var(--edge);
    box-sizing: border-box;
    overflow: hidden;
  }
  .band {
    position: absolute;
    left: 0;
    width: 100%;
    background:
      linear-gradient(100deg, var(--mist) 0%, var(--lilac) 26%, var(--slate) 44%, var(--steel) 56%, var(--dusk) 70%, var(--lilac) 86%, var(--slate) 100%);
  }
  .band--top { top: 0; height: 34px; }
  .band--bottom { bottom: 0; height: 116px; }
  .brand__mark {
    position: absolute;
    left: 134px;
    top: 127px;
    width: 112px;
    height: 105px;
    background: var(--navy);
  }
  .brand__name {
    position: absolute;
    left: 274px;
    top: 0;
    font-family: "Josefin Sans", sans-serif;
    font-weight: 400;
    line-height: 1;
    white-space: nowrap;
  }
  .brand__primary {
    position: absolute;
    top: 121px;
    left: 0;
    font-size: 70px;
    letter-spacing: 0;
    color: var(--navy);
  }
  .brand__secondary {
    position: absolute;
    top: 194px;
    left: 2px;
    font-size: 29px;
    letter-spacing: 10px;
    color: var(--grey);
  }
</style>
</head>
<body>
  <main class="canvas">
    <section class="card">
      <div class="band band--top" role="img" aria-label="Abstract faceted pattern in muted lilac, slate and steel blue"></div>
      <div class="brand__mark"></div>
      <div class="brand__name">
        <span class="brand__primary">PELLMORE</span>
        <span class="brand__secondary">ARCHITECTURE</span>
      </div>
      <div class="band band--bottom" role="img" aria-label="Abstract faceted pattern in muted lilac, slate and steel blue"></div>
    </section>
  </main>
</body>
</html>
```